Redesign of Engineering firm website

I want a redesign of the torvelpower.com website with the below in mind:

1- the client has a 3 main sectors: Renewable Energy, Process Automation and General Engineering.
2- Home page should show the 3 sectors
3- the other standard pages should be home, About, Clients, Projects, Training, Career, and Contact
4- The theme should be wordpress.
5- Responsive layout that works with all devices
6- One page layout is preferable for the home page.
7- it should be original and is not copied from other templates.
Updates

Reason: As requested from so many designers... the deadline is extended. Thank you

Target Market(s)

Engineers and professional

Industry/Entity Type

Solar Energy

Font styles to use
Serif
Sans Serif

Colors
3277b5
0355a3
0493ce

Requirements
Must have
• pictures that represent the three sectors

```html
<!DOCTYPE html>
<html lang="en">
<head>
<meta charset="utf-8">
<title>Torvel Power – Clean, Renewable Energy</title>
<link href="https://fonts.googleapis.com/css2?family=Montserrat:wght@400;600;700;800&family=Lato:wght@400;700&display=swap" rel="stylesheet">
<style>
:root{
  --blue:#0355a3;
  --blue-mid:#3277b5;
  --blue-light:#0493ce;
  --nav:#1e63b0;
  --field:#0a6bcc;
  --yellow:#fccb05;
  --sky:#d8ebfb;
  --grey-bg:#f1f1f1;
  --header-bg:#efefef;
  --text:#2a2a2a;
  --footer:#3a3a3a;
  --white:#ffffff;
}
*{margin:0;padding:0;box-sizing:border-box}
html,body{width:1200px;height:1200px;overflow:hidden;background:var(--white)}
body{font-family:'Lato',sans-serif;color:var(--text)}
.page{position:absolute;left:302px;top:0;width:596px;height:1200px;overflow:hidden}
.abs{position:absolute}

/* header */
.site-header{left:0;top:0;width:596px;height:46px;background:var(--header-bg)}
.brand{left:56px;top:13px;display:flex;align-items:center;gap:5px;font-family:'Montserrat',sans-serif;font-weight:700;font-size:19px;color:var(--blue-light);letter-spacing:.5px}
.brand-mark{width:7px;height:7px;background:var(--blue-light)}
.contact-chip{display:flex;align-items:center;gap:6px}
.chip-icon{width:23px;height:23px;border:1.5px solid var(--blue);border-radius:2px;display:flex;align-items:center;justify-content:center}
.phone{left:277px;top:11px}
.phone .num{font-family:'Montserrat',sans-serif;font-weight:700;font-size:11px;color:var(--blue)}
.phone .mail{font-family:'Montserrat',sans-serif;font-size:7px;color:var(--blue);margin-top:1px}
.addr{left:400px;top:11px}
.addr .lines{font-family:'Montserrat',sans-serif;font-weight:700;font-size:6.6px;color:var(--blue-light);line-height:10px}

/* nav */
.main-nav{left:0;top:46px;width:596px;height:21px;background:linear-gradient(#2a72bd,var(--nav))}
.nav-item{position:absolute;top:7px;font-family:'Montserrat',sans-serif;font-size:7px;color:var(--white);font-weight:500}
.nav-item .caret{display:inline-block;border-left:2.5px solid transparent;border-right:2.5px solid transparent;border-top:3px solid var(--white);margin-left:3px;vertical-align:middle}
.login{left:466px;top:0;width:75px;height:21px;background:var(--yellow);font-family:'Montserrat',sans-serif;font-weight:700;font-size:9px;color:var(--blue);display:flex;align-items:center;justify-content:center}

/* hero */
.hero{left:0;top:67px;width:596px;height:235px;background:radial-gradient(ellipse at 70% 40%,#5d6c80 0%,#3b4a61 50%,#27354d 100%)}
.hero-title{left:0;top:104px;width:596px;text-align:center;font-family:'Montserrat',sans-serif;font-weight:700;font-size:23px;color:var(--white)}
.hero-sub{left:130px;top:138px;width:336px;text-align:center;font-size:7px;line-height:11px;color:var(--white)}
.dropdown{left:142px;top:67px;width:178px;height:80px;background:var(--blue);padding-top:1px}
.dropdown li{list-style:none;font-family:'Montserrat',sans-serif;font-weight:600;font-size:5.8px;color:var(--white);height:12.6px;line-height:12.6px;padding-left:5px}
.dropdown li.active{background:var(--yellow);color:var(--blue);height:12px;line-height:12px}

/* sectors */
.sectors{left:0;top:302px;width:596px;height:226px;background:var(--grey-bg)}
.divider{top:0;width:1px;height:226px;background:#9bbbe0}
.sector{top:0;width:190px;height:226px;text-align:center}
.diamond{position:absolute;left:58px;top:29px;width:74px;height:74px;transform:rotate(45deg);background:linear-gradient(135deg,#6fbbf5 0%,#b9dcf8 55%,#ecf4fb 100%)}
.sector svg{position:absolute;left:70px;top:41px}
.sector h3{position:absolute;left:0;top:128px;width:190px;font-family:'Montserrat',sans-serif;font-weight:700;font-size:10.5px;color:var(--blue-mid)}
.sector p{position:absolute;left:24px;top:144px;width:142px;font-size:6.4px;line-height:10.8px;color:var(--text)}
.btn-more{position:absolute;left:62px;top:193px;width:66px;height:19px;background:var(--blue-mid);color:var(--white);font-family:'Montserrat',sans-serif;font-weight:700;font-size:6.6px;display:flex;align-items:center;justify-content:center}

/* about */
.about{left:0;top:528px;width:298px;height:170px;background:var(--yellow)}
.about h2{position:absolute;left:56px;top:16px;font-family:'Montserrat',sans-serif;font-weight:700;font-size:13.5px;color:var(--blue-mid)}
.about p{position:absolute;left:56px;top:39px;width:225px;font-size:6.3px;line-height:11.7px;color:var(--text)}
.photo-solar{left:298px;top:528px;width:298px;height:170px;background:linear-gradient(170deg,#4f8fd6 0%,#8fc0ec 38%,#1b5fb2 55%,#0b3f86 100%)}

/* projects */
.photo-team{left:0;top:698px;width:298px;height:192px;background:linear-gradient(180deg,#b9d3ec 0%,#cfd9e2 45%,#6e7a88 70%,#3c4654 100%)}
.projects{left:298px;top:698px;width:298px;height:192px;background:var(--sky)}
.projects h2{position:absolute;left:15px;top:12px;font-family:'Montserrat',sans-serif;font-weight:700;font-size:13.5px;color:var(--blue-mid)}
.projects ol{position:absolate;position:absolute;left:15px;top:39px;width:270px;list-style:none;font-size:7.1px;line-height:12.5px;color:var(--text)}

/* contact */
.contact{left:0;top:890px;width:596px;height:291px;background:var(--blue)}
.contact h2{position:absolute;left:56px;top:10px;font-family:'Montserrat',sans-serif;font-weight:700;font-size:13.5px;color:var(--white)}
.contact .info{position:absolute;left:58px;top:33px;font-size:6.4px;line-height:11.5px;color:var(--white)}
.field-label{position:absolute;left:56px;font-size:7.5px;color:var(--white)}
.field{position:absolute;left:100px;width:188px;height:17px;background:var(--field);border:1px solid #3d8be0}
.check{position:absolute;left:150px;top:235px;width:8px;height:8px;background:#cfd8e6;border-radius:1px}
.send{position:absolute;left:58px;top:252px;width:75px;height:22px;background:var(--yellow);color:var(--blue);font-size:8px;font-weight:700;display:flex;align-items:center;justify-content:center}
.map{position:absolute;left:298px;top:12px;width:243px;height:262px;background:linear-gradient(135deg,#f3f1ec,#e6e3dc)}

.site-footer{left:0;top:1181px;width:596px;height:19px;background:var(--footer);color:#d8d8d8;font-size:5.8px;display:flex;align-items:center;justify-content:center}
</style>
</head>
<body>
<div class="page">

  <header class="site-header abs">
    <div class="brand abs"><span class="brand-mark"></span>TORVEL</div>
    <div class="contact-chip phone abs">
      <div class="chip-icon">
        <svg width="13" height="13" viewBox="0 0 24 24"><path d="M6.6 10.8a15 15 0 0 0 6.6 6.6l2.2-2.2a1 1 0 0 1 1-.25 11.4 11.4 0 0 0 3.6.57 1 1 0 0 1 1 1V20a1 1 0 0 1-1 1A17 17 0 0 1 3 4a1 1 0 0 1 1-1h3.5a1 1 0 0 1 1 1c0 1.25.2 2.45.57 3.57a1 1 0 0 1-.25 1z" fill="#0355a3"/></svg>
      </div>
      <div><div class="num">+966100457200</div><div class="mail">info@torvelpower.com</div></div>
    </div>
    <div class="contact-chip addr abs">
      <div class="chip-icon">
        <svg width="11" height="14" viewBox="0 0 20 26"><path d="M10 1a8 8 0 0 0-8 8c0 6 8 15 8 15s8-9 8-15a8 8 0 0 0-8-8z" fill="none" stroke="#0355a3" stroke-width="2"/><circle cx="10" cy="9" r="3" fill="none" stroke="#0355a3" stroke-width="2"/></svg>
      </div>
      <div class="lines">Port Crescent, Eastern Province<br>40512 Kingdom of Saudi Arabia</div>
    </div>
  </header>

  <nav class="main-nav abs">
    <span class="nav-item" style="left:57px">HOME</span>
    <span class="nav-item" style="left:100px">ABOUT<span class="caret"></span></span>
    <span class="nav-item" style="left:146px">SERVICES<span class="caret"></span></span>
    <span class="nav-item" style="left:201px">TRAINING</span>
    <span class="nav-item" style="left:256px">EMPLOYMENT</span>
    <span class="nav-item" style="left:326px">CONTACT US</span>
    <div class="login abs">Log In</div>
  </nav>

  <section class="hero abs" role="img" aria-label="Wind turbines at dusk under a blue-grey sky">
    <h1 class="hero-title abs">CLEAN, RENEWABLE ENERGY</h1>
    <p class="hero-sub abs">Nulla eget ipsum id est accumsan pellentesque nec et odio. Duis sit amet convallis sem, tincidunt feugiat lorem. Nunc porttitor arcu ac dui aliquam efficitur.</p>
  </section>

  <ul class="dropdown abs">
    <li class="active">Solar Consulting Services</li>
    <li>Feasiblity Studies</li>
    <li>RFP and RFQ Development</li>
    <li>Due Diligence Services</li>
    <li>Design and Engineering development</li>
    <li>Solar System Operations &amp; Maintenance and Monitoring</li>
  </ul>

  <section class="sectors abs">
    <div class="divider abs" style="left:217px"></div>
    <div class="divider abs" style="left:379px"></div>

    <article class="sector abs" style="left:40px">
      <div class="diamond"></div>
      <svg width="50" height="50" viewBox="0 0 50 50">
        <path d="M6 28 L17 18 L28 28 V42 H22 V34 H14 V42 H6 Z" fill="#0a62b8"/>
        <rect x="33" y="16" width="2.5" height="26" fill="#0a62b8"/>
        <path d="M34 16 L26 10 L34 14 L40 5 L35 15 L44 18 Z" fill="#0a62b8"/>
        <path d="M42 26 q4 -5 0 -10 M45 28 q6 -8 0 -15" stroke="#0a62b8" stroke-width="1.6" fill="none"/>
      </svg>
      <h3>Renewable Energy</h3>
      <p>Lorem Ipsum is simply dummy text of the printing and typesetting industry. Lorem Ipsum has been the industry's standard dummy text ever since the 1500s.</p>
      <div class="btn-more">Read More..</div>
    </article>

    <article class="sector abs" style="left:203px">
      <div class="diamond"></div>
      <svg width="50" height="50" viewBox="0 0 50 50">
        <rect x="14" y="36" width="20" height="6" fill="#0a62b8"/>
        <path d="M20 36 L14 20 L19 18 L25 36 Z" fill="#0a62b8"/>
        <circle cx="15" cy="16" r="5" fill="none" stroke="#0a62b8" stroke-width="3"/>
        <path d="M19 14 L32 12" stroke="#0a62b8" stroke-width="4"/>
        <path d="M32 8 L40 6 L42 10 L36 12 L42 14 L40 18 L32 16 Z" fill="#0a62b8"/>
      </svg>
      <h3>Process Automation</h3>
      <p>Lorem Ipsum is simply dummy text of the printing and typesetting industry. Lorem Ipsum has been the industry's standard dummy text ever since the 1500s.</p>
      <div class="btn-more">Read More..</div>
    </article>

    <article class="sector abs" style="left:366px">
      <div class="diamond"></div>
      <svg width="50" height="50" viewBox="0 0 50 50">
        <path d="M12 10 a6 6 0 0 0 6 9 L34 35 L38 31 L22 15 a6 6 0 0 0 -9 -6 l4 4 -2 3 -3 -1 z" fill="#0a62b8"/>
        <rect x="28" y="30" width="12" height="10" rx="3" transform="rotate(40 34 35)" fill="#3a8ee0"/>
      </svg>
      <h3>General Engineering</h3>
      <p>Lorem Ipsum is simply dummy text of the printing and typesetting industry. Lorem Ipsum has been the industry's standard dummy text ever since the 1500s.</p>
      <div class="btn-more">Read More..</div>
    </article>
  </section>

  <section class="about abs">
    <h2>About Us</h2>
    <p>We are the solar experts in the solar kingdom. The KSA (Saudi Arabia) solar market is a promising market with huge potential. The plan is to build 41,000 MW of solar in the coming 20 years, as announced by N.S.E.A. (National Solar Energy Authority). We provide our services, both by our in-house team and associated partners. All together have diversified expertise covering various aspects of solar PV. We cover all technology, market and finance related aspects of solar PV. Our network of government officials, real estate experts, market analyst, and industry professionals track the market in real time, and turn knowledge to experience and value to our clients.</p>
  </section>
  <div class="photo-solar abs" role="img" aria-label="Solar panel field with wind turbines under a blue sky"></div>

  <div class="photo-team abs" role="img" aria-label="Two engineers with a laptop inspecting rooftop solar panels"></div>
  <section class="projects abs">
    <h2>Our Projects</h2>
    <ol>
      <li>1. Gulf Tech Institute Energy Efficiency Study for GTIP.</li>
      <li>2. NSEA Solar Atlas</li>
      <li>3. NSEA Irradiation data Development</li>
      <li>4. Coastal University Digital Energy meter for Residential campus</li>
      <li>5. Embassy District Energy Data consumption</li>
      <li>6. CMH Energy Efficiency</li>
      <li>7. Brightwave Solar analysis support for GCC new installation</li>
      <li>8. Electrical Grounding Courses</li>
      <li>9. PERC projects as references (4) projects</li>
      <li>10. Developing Short Video clips for events and illustrating engineering concepts</li>
    </ol>
  </section>

  <section class="contact abs">
    <h2>Conatct Detail</h2>
    <div class="info">Port Crescent, Eastern Province 40512 Kingdom of Saudi Arabia<br>info@torvelpower.com<br>+966100457200</div>

    <span class="field-label" style="top:82px">Name *</span>
    <div class="field" style="top:79px"></div>
    <span class="field-label" style="top:107px">Email *</span>
    <div class="field" style="top:104px"></div>
    <span class="field-label" style="top:132px">Subject *</span>
    <div class="field" style="top:128px"></div>
    <span class="field-label" style="top:157px">Message *</span>
    <div class="field" style="top:154px;height:70px"></div>

    <span class="field-label" style="top:232px">Send Copy To yourself</span>
    <div class="check"></div>
    <div class="send">Send Email</div>

    <div class="map" role="img" aria-label="Street map showing the office location"></div>
  </section>

  <footer class="site-footer abs">Copyright © 2014 TORVEL POWER CONSULTING, All rights reserved.</footer>
</div>
</body>
</html>
```